Business cards for education company

We need a business card design for a relatively new company based in Queensland and operating across Australia. We resell diploma level education courses which include Business, Management, Finance, Community Services & Government courses. We offer over 20 different courses.
The target market is for anyone 16 years of age and older. There is no age limit.

We would like to see the design use the color blue and silver. The final design should communicate professionalism and a bright future.

We sell education but are also promoting the career they see themselves in 2-3 years in the future

Our company logo is attached.

Target Market(s)

We target all age groups above 16 years of age. The main target market would be people aged between 17-35.

We focus on those people who cannot make it into University or do not want to commit the time to a full degree.

Industry/Entity Type

Education

Requirements
Must have
• Professional
Company logo
website
Contact details:

Please use the following example:

Lionel Tapping
Senior Education Consultant
0417 385 960
Lionel.tapping@skylarklearninghub.com.au
www.skylarklearninghub.com.au

```html
<!DOCTYPE html>
<html lang="en">
<head>
<meta charset="utf-8">
<title>Lionel Tapping – Skylark Learning Hub Business Card</title>
<link href="https://fonts.googleapis.com/css2?family=Lato:wght@400;700&display=swap" rel="stylesheet">
<style>
  :root {
    --card-bg: #fdfefe;
    --ink-blue: #1b1f8f;
    --brand-blue: #1f5fbf;
    --silver: #9aa3a3;
    --diamond-silver: #eef0f0;
    --diamond-blue: #c4c9f8;
    --divider: #1f5fbf;
  }
  html, body {
    margin: 0;
    padding: 0;
    width: 1200px;
    height: 741px;
    overflow: hidden;
    background: var(--card-bg);
  }
  .business-card {
    position: relative;
    width: 1200px;
    height: 741px;
    background: var(--card-bg);
    font-family: "Lato", "Gill Sans", sans-serif;
    overflow: hidden;
  }
  .diamond-motif {
    position: absolute;
    inset: 0;
  }
  .brand {
    position: absolute;
    left: 78px;
    top: 84px;
    height: 134px;
    display: flex;
    align-items: center;
  }
  .brand-mark {
    width: 110px;
    height: 110px;
    border-radius: 50%;
    background: var(--brand-blue);
    margin-left: 36px;
    margin-right: 60px;
  }
  .brand-divider {
    width: 2px;
    height: 134px;
    background: var(--divider);
    margin-right: 14px;
  }
  .brand-name {
    font-family: "Lato", sans-serif;
    font-weight: 700;
    font-size: 30px;
    line-height: 1.15;
    color: var(--brand-blue);
    text-transform: uppercase;
    letter-spacing: 0.5px;
    width: 230px;
  }
  .consultant {
    position: absolute;
    right: 85px;
    top: 108px;
    text-align: right;
  }
  .consultant-name {
    margin: 0;
    font-weight: 400;
    font-size: 41px;
    line-height: 1.1;
    color: var(--ink-blue);
  }
  .consultant-title {
    margin: 4px 0 0;
    font-size: 31px;
    color: var(--silver);
  }
  .contact-details {
    position: absolute;
    right: 85px;
    top: 544px;
    text-align: right;
    font-size: 28px;
    line-height: 39px;
    color: var(--ink-blue);
  }
  .contact-details p { margin: 0; }
</style>
</head>
<body>
  <main class="business-card">
    <svg class="diamond-motif" width="1200" height="741" viewBox="0 0 1200 741" aria-hidden="true">
      <polygon points="306,216 527,437 306,658 85,437" fill="var(--diamond-silver)"/>
      <polygon points="899,216 1119,436 899,656 679,436" fill="var(--diamond-silver)"/>
      <polygon points="610,216 829,435 610,654 391,435" fill="var(--diamond-blue)" opacity="0.92"/>
    </svg>

    <div class="brand">
      <span class="brand-mark"></span>
      <span class="brand-divider"></span>
      <span class="brand-name">Skylark Learning Hub</span>
    </div>

    <header class="consultant">
      <h1 class="consultant-name">Lionel Tapping</h1>
      <p class="consultant-title">Senior Education Consultant</p>
    </header>

    <address class="contact-details" style="font-style: normal;">
      <p class="contact-phone">Tel: 0417 385 960</p>
      <p class="contact-email">Email: Lionel.tapping@skylarklearninghub.com.au</p>
      <p class="contact-web">www.skylarklearninghub.com.au</p>
    </address>
  </main>
</body>
</html>
```